Book Cover For An Investment Book On Trend Trading

We are in need of a clean modern book cover with a modern feel for a new book on trend trading.

Task Description
I need a book cover for traditional print and eReaders (Lumora, etc.) for a new financial investment book targeted at people who want to manage their own money. The title is “A Quick Primer for Portfolio Growth” with subtitle “Riding Upswings and Dodging Slumps Wisely” written by, Gordon Pike.

In brief, simple techniques to identify the direction of the market and then actionable steps to trade with the trend for financial success are shown. No more endless roller coaster ride watching your investments rise and then precipitously fall.

There is discussion about famous historic and recent bubbles and human nature. The poor performance of a number of hedge funds is reviewed and suggest the smartest person in the room may be you managing you own money.

This is a practical, hands-on guide targeted at the novice to intermediate experienced investor.

Note: We have a temp logo attached. If you want to create a new one, feel free.

www.steadyslopemarkets.com

Please include in the design a picture of the author an description. Use place holder for now.

Please also include 3 testimonials.
Updates

The dimensions are 8.5 x 5.5 x .75

Industry/Entity Type

Financial

Requirements
Nice to have
• Three testimonials

Author Pic (use place holder)
and back ground

A Graphic of trend lines on A recent Birchfield Stock Chart or VORNA. (Go to finderly and type in Birchfield Stock and trend lines.)

```html
<!DOCTYPE html>
<html lang="en">
<head>
<meta charset="utf-8">
<title>A Quick Primer for Portfolio Growth — Book Cover</title>
<link rel="stylesheet" href="https://fonts.googleapis.com/css2?family=Anton&family=Archivo+Black&family=Open+Sans:wght@400;700&family=Roboto+Condensed:wght@700&family=Arimo:wght@700&display=swap">
<style>
  :root {
    --stage: #4a4a4c;
    --navy-deep: #1a1a5e;
    --navy: #22237a;
    --royal: #2a3c9c;
    --sky: #1aa3e6;
    --sky-light: #35b6ef;
    --band-grey: #7a7a86;
    --lavender: #8f8fc6;
    --ink: #111133;
    --white: #ffffff;
  }
  * { box-sizing: border-box; margin: 0; padding: 0; }
  html, body { width: 1200px; height: 999px; overflow: hidden; }
  body {
    background: var(--stage);
    font-family: "Open Sans", Arial, sans-serif;
    position: relative;
  }
  .book-spread {
    position: absolute;
    left: 70px; top: 100px;
    width: 1060px; height: 800px;
    display: flex;
  }
  /* Back cover */
  .back-cover {
    width: 490px; height: 100%;
    background: linear-gradient(180deg, var(--navy-deep) 0%, var(--navy) 35%, var(--royal) 55%, var(--sky) 85%, var(--sky-light) 100%);
    color: var(--white);
    padding: 42px 40px 30px 40px;
    position: relative;
  }
  .back-heading {
    font-weight: 700;
    font-size: 25px;
    margin-bottom: 12px;
  }
  .back-text {
    font-size: 12.3px;
    line-height: 1.5;
    text-align: justify;
    margin-bottom: 20px;
  }
  .author-section { position: absolute; left: 40px; right: 40px; top: 470px; }
  .author-row { display: flex; gap: 18px; }
  .author-row .back-text { flex: 1; }
  .author-photo-placeholder {
    width: 132px; height: 175px;
    background: var(--white);
    border-radius: 16px;
    flex: none;
    margin-top: -28px;
  }
  .website {
    position: absolute; right: 40px; bottom: 92px;
    font-size: 12.5px;
  }
  /* Spine */
  .spine {
    width: 80px; height: 100%;
    background: linear-gradient(90deg, var(--sky) 0%, var(--royal) 55%, var(--navy) 100%);
    position: relative;
  }
  .spine-title {
    position: absolute; top: 50%; left: 50%;
    transform: translate(-50%, -50%) rotate(90deg);
    white-space: nowrap;
    color: var(--white);
    font-family: "Roboto Condensed", "Arial Narrow", sans-serif;
    font-weight: 700;
    font-size: 27px;
  }
  /* Front cover */
  .front-cover {
    width: 490px; height: 100%;
    background: var(--navy);
    display: flex; flex-direction: column;
  }
  .title-block {
    height: 270px;
    background: linear-gradient(180deg, var(--sky) 0%, var(--royal) 55%, var(--navy) 100%);
    color: var(--white);
    text-align: center;
    padding-top: 18px;
    line-height: 1;
  }
  .title-line-top { font-family: "Anton", Impact, sans-serif; font-size: 66px; display: block; }
  .title-line-mid { font-family: "Archivo Black", "Arial Black", sans-serif; font-size: 36px; display: block; margin: 6px 0 4px; }
  .title-line-main { font-family: "Anton", Impact, sans-serif; font-size: 88px; display: block; }
  .divider-stripe { height: 12px; background: var(--band-grey); }
  .chart-art {
    height: 330px;
    background: linear-gradient(160deg, #1d2d8a 0%, #2f4bb8 45%, #3d5fd0 70%, #1e2a80 100%);
  }
  .subtitle-band {
    height: 110px;
    background: linear-gradient(180deg, var(--sky-light), var(--sky));
    color: var(--navy-deep);
    font-family: "Arimo", Arial, sans-serif;
    font-weight: 700;
    font-size: 27px;
    text-transform: uppercase;
    text-align: center;
    line-height: 1.2;
    display: flex; align-items: center; justify-content: center;
  }
  .author-band {
    height: 45px;
    background: var(--lavender);
    color: var(--ink);
    font-family: "Arimo", Arial, sans-serif;
    font-weight: 700;
    font-size: 25px;
    text-align: center;
    line-height: 45px;
  }
  .bottom-band { flex: 1; background: var(--navy); }
</style>
</head>
<body>
  <main class="book-spread">
    <section class="back-cover">
      <h2 class="back-heading">Testimonials</h2>
      <p class="back-text">Lorem ipsum dolor sit amet, consectetur adipiscing elit. Curabitur lacinia congue varius. Nunc ut augue cursus lectus aliquet elementum. Suspendisse semper sodales eros id cursus. Nunc lacinia adipiscing nibh. Maecenas eu dui velit. Sed nec sem leo. In a lacus scelerisque, condimentum turpis a, mollis orci. Integer nec orci justo. Nulla non dolor neque. Etiam condimentum erat sem, et posuere orci aliquam pellentesque. In nec ante quis urna gravida interdum. In lobortis elementum neque, nec interdum purus blandit sed. Curabitur adipiscing suscipit nunc ac molestie.</p>
      <p class="back-text">Lorem ipsum dolor sit amet, consectetur adipiscing elit. Curabitur lacinia congue varius. Nunc ut augue cursus lectus aliquet elementum. Suspendisse semper sodales eros id cursus. Nunc lacinia adipiscing nibh. Maecenas eu dui velit. Sed nec sem leo. In a lacus scelerisque, condimentum turpis a, mollis orci. Integer nec orci justo. Nulla non dolor neque. Etiam condimentum erat sem, et posuere orci aliquam pellentesque. In nec ante quis urna gravida interdum. In lobortis elementum neque, nec interdum purus blandit sed. Curabitur adipiscing suscipit nunc ac molestie.</p>
      <div class="author-section">
        <h2 class="back-heading">Author</h2>
        <div class="author-row">
          <p class="back-text">Lorem ipsum dolor sit amet, consectetur adipiscing elit. Curabitur lacinia congue varius. Nunc ut augue cursus lectus aliquet elementum. Suspendisse semper sodales eros id cursus. Nunc lacinia adipiscing nibh. Maecenas eu dui velit. Sed nec sem leo. In a lacus scelerisque, condimentum turpis a, mollis orci. Integer nec orci justo. Nulla non dolor neque. Etiam condimentum erat sem, et neque.</p>
          <div class="author-photo-placeholder" role="img" aria-label="Author photo placeholder"></div>
        </div>
      </div>
      <p class="website">www.steadyslopemarkets.com</p>
    </section>

    <section class="spine">
      <span class="spine-title">A Quick Primer for Portfolio Growth</span>
    </section>

    <section class="front-cover">
      <h1 class="title-block">
        <span class="title-line-top">A QUICK PRIMER</span>
        <span class="title-line-mid">FOR PORTFOLIO</span>
        <span class="title-line-main">GROWTH</span>
      </h1>
      <div class="divider-stripe"></div>
      <div class="chart-art" role="img" aria-label="Glowing stock market chart with candlesticks and trend lines on a blue grid"></div>
      <div class="divider-stripe"></div>
      <p class="subtitle-band">Riding Upswings and<br>Dodging Slumps Wisely</p>
      <p class="author-band">Gordon Pike</p>
      <div class="bottom-band"></div>
    </section>
  </main>
</body>
</html>
```